Business Card Design Project

I need a new business card design for my building/development company: Kestrel Ridge Builders.

We specialise in small sub-divisions, multi-story developments and new house builds.
We handle the whole process from concept stage right throught to a fully developed property.
Updates

Target Market(s)

people looking to develop their property and need help. New property buyers

Industry/Entity Type

House

Requirements
Must have
• My logo on both sides:
Side 1: Logo taking up whole side as per old card but with a color/style change.

Side 2: Contact page: include logo but the rest just surprise me!

All contact details will be: (and need to be changable for each employee) I'll inform you of specifics before printing.

Name Surname
Position ie. Managing director
M: insert mobile
E: insert email
P.O. Box 518, Ashwell, Vic, 3094
www.kestrelridgebuilders.com.au

Nice to have
• Colors i'd like: (not necessarily all but this is the basic idea)

Black, blue, grey, silver, white

```html
<!DOCTYPE html>
<html lang="en">
<head>
<meta charset="utf-8">
<title>Kestrel Ridge Builders – Business Card</title>
<link rel="stylesheet" href="https://fonts.googleapis.com/css2?family=Source+Sans+3:wght@400;600;700&display=swap">
<style>
  :root {
    --stage: #e6e7e9;
    --card-white: #ffffff;
    --brand-blue: #1b8fd8;
    --band-blue: #0a8fd6;
    --band-light: #eef7fd;
    --ink: #111111;
    --soft-edge: #c9ccd0;
    --back-deep: #1f9ae0;
    --back-mid: #8fcbf0;
    --back-light: #ffffff;
  }
  * { margin: 0; padding: 0; box-sizing: border-box; }
  html, body {
    width: 954px; height: 1200px; overflow: hidden;
    background: var(--stage);
    font-family: "Source Sans 3", "Myriad Pro", Arial, sans-serif;
    color: var(--ink);
  }
  .canvas { position: relative; width: 954px; height: 1200px; }

  .card {
    position: absolute; width: 800px; height: 466px;
    border-radius: 30px; overflow: hidden;
    border: 1px solid var(--soft-edge);
  }

  .brand-mark {
    position: absolute; left: 50%; transform: translateX(-50%);
    background: var(--brand-blue);
  }

  .wordmark {
    position: absolute; left: 0; right: 0; text-align: center;
    font-weight: 600; line-height: 1; white-space: nowrap;
  }
  .tagline {
    position: absolute; left: 0; right: 0; text-align: center;
    font-weight: 400; line-height: 1; color: var(--ink); letter-spacing: 0.3px;
  }

  /* Contact side */
  .card--front { top: 67px; left: 82px; background: var(--card-white); }
  .card--front .brand-mark { top: 42px; width: 112px; height: 112px; }
  .card--front .wordmark { top: 184px; font-size: 46px; color: var(--brand-blue); }
  .card--front .tagline { top: 231px; font-size: 20px; }

  .name-band {
    position: absolute; top: 282px; left: 0; width: 684px; height: 55px;
    background: linear-gradient(90deg, var(--band-blue) 0%, #5fb6ea 22%, var(--band-light) 42%, #7cc4ee 62%, var(--band-blue) 85%);
    display: flex; align-items: center; padding-left: 181px;
  }
  .name-band .person { font-size: 25px; font-weight: 400; color: var(--ink); }
  .name-band .role { font-size: 19px; color: var(--ink); }
  .end-block {
    position: absolute; top: 282px; left: 695px; right: 0; height: 55px;
    background: var(--ink);
  }

  .contacts {
    position: absolute; top: 378px; left: 67px; right: 24px;
    display: grid; grid-template-columns: 349px auto; row-gap: 12px;
    font-size: 18px; line-height: 22px; white-space: nowrap;
  }
  .contacts b { font-weight: 700; }

  /* Logo side */
  .card--back {
    top: 681px; left: 79px;
    background: radial-gradient(ellipse 62% 70% at 52% 55%, var(--back-light) 0%, #dff0fb 35%, var(--back-mid) 70%, var(--back-deep) 100%);
  }
  .card--back .brand-mark { top: 88px; width: 176px; height: 176px; }
  .card--back .wordmark { top: 290px; font-size: 58px; color: var(--ink); }
  .card--back .tagline { top: 348px; font-size: 25px; }
</style>
</head>
<body>
<main class="canvas">

  <section class="card card--front" aria-label="Business card, contact side">
    <div class="brand-mark" aria-hidden="true"></div>
    <div class="wordmark">Kestrel Ridge Builders</div>
    <div class="tagline">renovation-construction-development</div>

    <div class="name-band">
      <span class="person">Your Name -&nbsp;</span><span class="role">Managing director</span>
    </div>
    <div class="end-block"></div>

    <div class="contacts">
      <span><b>e</b> : info@kestrelridgebuilders.com.au</span>
      <span><b>m</b> : 0400 555 219</span>
      <span><b>w</b> : www.kestrelridgebuilders.com.au</span>
      <span>P.O. Box 518, Ashwell, Vic, 3094</span>
    </div>
  </section>

  <section class="card card--back" aria-label="Business card, logo side">
    <div class="brand-mark" aria-hidden="true"></div>
    <div class="wordmark">Kestrel Ridge Builders</div>
    <div class="tagline">renovation-construction-development</div>
  </section>

</main>
</body>
</html>
```